Corvana Power Holdings Website

We have color scheme, logo and content, but need a design options in PDF format for the website. The PDF should guide us in how to use the color scheme and fonts in the site design (what background colors to use where, what link and hover colors to you, when to use which fonts...)

Corvana Power Holdings wants a conservative and straightforward website design that is in line with the banking industry. At the same time, Corvana wants the design to be innovative and cutting-edge in line with the renewable energy industry. Overall, the site design must be present the company as professional, serious, knowledgeable, experienced, reliable, and successful as well as a global good citizen.
Updates

We are closing this project. Thank you all for your beautiful work. Our designer was sick, but informed us today that she is better and able to resume her work. So we are closing this project and restarting work with her. Wish you all health and success.

Target Market(s)

investors, partners, developers, investment community, private equity community

Industry/Entity Type

Investment

Number of Pages Required

2 page

Requirements
Must have
• The color scheme is attached.
The logo is attached.
Fonts are Questrial and Cormorant (as used in logo).
The site must use these colors and fonts and logo design.

The 2 pages we need designed are the homepage and the portfolio page.
Homepage - The portfolio map on the homepage will be an image like with hotspots that link to portfolio items. This map image might go well with logo:
https://www.pixdrovo.com/abstract-polygon-world-map-vector-illustration-geometric-structure-in-blue-color-for-presentation-booklet-website-and-other-design-projects-pol-image550392817.html
But we would need to zoom in on Israel and EU, and leave out US / Asia-Pacific.
The way the map will work technically (using hotspots) should be something like:
https://tarvimpower.co.il/geographic-spread/.
Portfolio Page - The portfolio map there will be a Google Map/
Nice to have
• The content for the site is attached as a Word Doc, and much of it is in place at http://corvanafund.com.node4821.hostmarvo.de/. The design must fit this content, but we are open to some layout changes.
Design Requests:
• nav bar – light animation like https://pelludovet.com/ and https://www.qz-relocationlaw.com/
• innovative, unique design with welcoming, appealing, modern feel
• engaging content display by using parallax and subtle movement
• clean, intuitive, easy to navigation layout

```html
<!DOCTYPE html>
<html lang="en">
<head>
<meta charset="utf-8">
<title>Corvana Power Holdings</title>
<link rel="stylesheet" href="https://fonts.googleapis.com/css2?family=Cormorant:wght@500;600;700&family=Questrial&display=swap">
<style>
:root{
  --ink:#0c3b36;
  --text:#1f2d2b;
  --muted:#8a8f93;
  --line:#d9dcdc;
  --white:#ffffff;
  --sun:#fde13a;
  --orange:#f7a85f;
  --ocean:#0d86b3;
  --leaf:#7fcf1f;
  --hero-left:#d8ef5a;
  --hero-mid:#a8ecc4;
  --hero-right:#4fc6f2;
}
*{box-sizing:border-box;margin:0;padding:0}
html,body{width:1200px;height:904px;overflow:hidden;background:var(--white)}
body{position:relative;font-family:"Questrial",sans-serif;color:var(--text)}
.hero{position:absolute;left:0;top:0;width:1200px;height:642px;overflow:hidden}
.hero-photo{position:absolute;inset:0;background:
  radial-gradient(ellipse 420px 260px at 600px 560px,rgba(255,255,255,.45),transparent 70%),
  linear-gradient(180deg,transparent 70%,rgba(190,225,90,.55) 100%),
  linear-gradient(90deg,var(--hero-left) 0%,var(--hero-mid) 50%,var(--hero-right) 100%)}
.site-nav{position:absolute;top:34px;left:0;width:1200px;height:34px}
.nav-link{position:absolute;top:10px;font-family:"Cormorant",serif;font-weight:600;font-size:12.5px;letter-spacing:.8px;color:var(--ink);text-decoration:none}
.brand{position:absolute;left:512px;top:0;display:flex;align-items:center;gap:8px}
.brand-dot{width:30px;height:30px;border-radius:50%;background:var(--sun)}
.brand-name{font-family:"Cormorant",serif;font-weight:700;font-size:30px;line-height:1;color:var(--ink);letter-spacing:.5px}
.search{position:absolute;left:1043px;top:9px}
.hero-title{position:absolute;top:132px;width:1200px;text-align:center;font-family:"Cormorant",serif;font-weight:700;font-size:40px;letter-spacing:1.5px;color:var(--ink)}
.hero-sub{position:absolute;top:188px;width:1200px;text-align:center;font-size:19.5px;color:var(--ink)}
.portfolio-map{position:absolute;left:221px;top:224px;width:757px;height:260px;border-radius:40px;
  background:radial-gradient(ellipse at center,rgba(255,255,255,.55),rgba(255,255,255,.12) 75%,transparent)}
.stats{position:absolute;top:485px;left:144px;display:flex;gap:23px}
.stat{width:211px;height:96px;background:var(--white);display:flex;align-items:center;padding-left:25px}
.stat-icon{width:44px;height:44px;border-radius:50%;display:flex;align-items:center;justify-content:center;flex:none}
.stat-body{margin-left:15px;margin-top:-4px}
.stat-value{font-size:23px;line-height:1.1;color:var(--text)}
.stat-label{font-size:11px;line-height:14px;color:var(--muted);margin-top:6px;width:80px}
.stat-label.wide{width:110px}
.footer-brand{position:absolute;left:144px;top:682px;display:flex;align-items:center;gap:9px}
.footer-brand .brand-dot{width:40px;height:40px}
.footer-brand .brand-name{font-size:34px}
.footer-nav{position:absolute;right:144px;top:698px;display:flex;gap:26px}
.footer-nav a{font-family:"Cormorant",serif;font-weight:600;font-size:12px;letter-spacing:.6px;color:var(--ink);text-decoration:none}
.divider{position:absolute;left:144px;top:763px;width:912px;height:1px;background:var(--line)}
.contacts{position:absolute;top:802px;left:144px;display:flex}
.contact{width:234px;display:flex;gap:12px;font-size:10.6px;line-height:17.6px;color:var(--text)}
.contact svg{flex:none}
</style>
</head>
<body>
<section class="hero">
  <div class="hero-photo" role="img" aria-label="Wind turbines on a green hillside under a bright sky, tinted yellow-green to sky blue"></div>
  <nav class="site-nav">
    <a class="nav-link" style="left:341px" href="#">ABOUT</a>
    <a class="nav-link" style="left:417px" href="#">STRATEGY</a>
    <div class="brand"><span class="brand-dot"></span><span class="brand-name">Corvana</span></div>
    <a class="nav-link" style="left:722px" href="#">PORTFOLIO</a>
    <a class="nav-link" style="left:824px" href="#">CONTACT</a>
    <svg class="search" width="14" height="14" viewBox="0 0 14 14" fill="none" stroke="#0c3b36" stroke-width="1.8"><circle cx="5.5" cy="5.5" r="4"/><path d="M8.5 8.5l4.5 4.5"/></svg>
  </nav>
  <h1 class="hero-title">ILLUMINATING THE FUTURE</h1>
  <p class="hero-sub">Investing in clean energy to generate sustainable returns for our investors and planet</p>
  <div class="portfolio-map" role="img" aria-label="Dotted world map with portfolio hotspots across Europe and Israel"></div>
  <div class="stats">
    <div class="stat">
      <span class="stat-icon" style="background:var(--sun)"><svg width="24" height="22" viewBox="0 0 24 22" fill="none" stroke="#fff" stroke-width="1.5"><rect x="2" y="4" width="20" height="16" rx="2"/><path d="M2 9h20M7 2v4M12 2v4M17 2v4M6 12h3M11 12h3M16 12h3M6 16h3M11 16h3M16 16h3"/></svg></span>
      <div class="stat-body"><div class="stat-value">10</div><div class="stat-label wide">Years of Operation</div></div>
    </div>
    <div class="stat">
      <span class="stat-icon" style="background:var(--orange)"><svg width="22" height="24" viewBox="0 0 22 24" fill="none" stroke="#fff" stroke-width="1.5"><path d="M5 2v21M5 3h13l-3 5 3 5H5"/></svg></span>
      <div class="stat-body"><div class="stat-value">6</div><div class="stat-label">Countries of Investments</div></div>
    </div>
    <div class="stat">
      <span class="stat-icon" style="background:var(--ocean)"><svg width="26" height="26" viewBox="0 0 26 26" fill="none" stroke="#fff" stroke-width="1.4"><circle cx="13" cy="13" r="6.5"/><path d="M13 2v3M13 21v3M2 13h3M21 13h3M5.2 5.2l2.1 2.1M18.7 18.7l2.1 2.1M5.2 20.8l2.1-2.1M18.7 7.3l2.1-2.1M10 13l2 2 4-4"/></svg></span>
      <div class="stat-body"><div class="stat-value">600</div><div class="stat-label">MW under Management</div></div>
    </div>
    <div class="stat">
      <span class="stat-icon" style="background:var(--leaf)"><svg width="26" height="26" viewBox="0 0 26 26" fill="none" stroke="#fff" stroke-width="1.4"><circle cx="13" cy="13" r="6.5"/><path d="M13 2v3M13 21v3M2 13h3M21 13h3M5.2 5.2l2.1 2.1M18.7 18.7l2.1 2.1M5.2 20.8l2.1-2.1M18.7 7.3l2.1-2.1M10 13l2 2 4-4"/></svg></span>
      <div class="stat-body"><div class="stat-value">500 M</div><div class="stat-label">Assets under Management</div></div>
    </div>
  </div>
</section>

<footer>
  <div class="footer-brand"><span class="brand-dot"></span><span class="brand-name">Corvana</span></div>
  <nav class="footer-nav">
    <a href="#">HOME</a><a href="#">ABOUT</a><a href="#">STRATEGY</a><a href="#">PORTFOLIO</a><a href="#">CONTACT US</a>
  </nav>
  <div class="divider"></div>
  <div class="contacts">
    <div class="contact">
      <svg width="22" height="28" viewBox="0 0 22 28"><path d="M11 1C5.5 1 2 5 2 10c0 6 9 17 9 17s9-11 9-17c0-5-3.5-9-9-9z" fill="var(--sun)"/><circle cx="11" cy="10" r="3.2" fill="#fff"/></svg>
      <span>Corvana Power Holdings,<br>Meridian House, Ha'Oren Street,<br>Kfar Tavor 15241 Israel</span>
    </div>
    <div class="contact">
      <svg width="26" height="20" viewBox="0 0 26 20" fill="none" stroke="var(--orange)" stroke-width="1.5"><rect x="1" y="1" width="24" height="18"/><path d="M1 1l12 10L25 1M1 19l9-9M25 19l-9-9"/></svg>
      <span>info@corvanafund.com</span>
    </div>
    <div class="contact">
      <svg width="26" height="26" viewBox="0 0 26 26" fill="none" stroke="var(--ocean)" stroke-width="1.5"><circle cx="13" cy="13" r="11.5"/><path d="M9 7l2.5 3-1.5 2c1 2 2.5 3.5 4 4l2-1.5 3 2.5-1.5 2.5c-5 0-10-5-10.5-10.5z"/><path d="M15 6a6 6 0 015 5M15 9a3 3 0 012 2"/></svg>
      <span>Israel: +972-3-555-0148</span>
    </div>
    <div class="contact">
      <svg width="26" height="26" viewBox="0 0 26 26" fill="none" stroke="var(--leaf)" stroke-width="1.5"><circle cx="13" cy="13" r="11.5"/><path d="M9 7l2.5 3-1.5 2c1 2 2.5 3.5 4 4l2-1.5 3 2.5-1.5 2.5c-5 0-10-5-10.5-10.5z"/><path d="M15 6a6 6 0 015 5M15 9a3 3 0 012 2"/></svg>
      <span>Europe: +44 (0) 20 7946 0321</span>
    </div>
  </div>
</footer>
</body>
</html>
```